larkwind flakies snack packaging

We are a new startup snack company that need a design for a snack packaging. Our snack goes by the name of larkwind flakies. Its a traditional snack usually eaten during festive seasons in south east asia region. The idea is to revolutionize the notion of the snack from one that is eaten during these celebratory seasons to an everyday one. The packaging design should be modern and minimalist yet fun too, also taking into consideration that it should not appear to be too childish. It should stand out from the other snacks products like potato chips etc if placed on the same shelf. The colour scheme is not decided yet as we are open to more ideas but colours should be complementary and not more than 2 or 3 hopefully. There should be also be an enthic sense of south east asian features on the design and it should reflects the Chinese, Malay and indian heritage. It need not be too obvious, a subtle kind should suffice. The packaging should also have the particular graphic/shape of the mould that i have upload followed by the picture of the snack. I have included a mock up of the logo of my company. Proposed designs can feel free to alter the larkwind graphic to a more modern, minimalist yet whimsical and fun. Proposed designs should have a front and back view of the packaging. We are looking to launch at 4 to 5 flavours like white sesame, black sesame, peanuts with white sesame and original.
Updates

Project Deadline Extended
Reason: Not enough submissions coming in yet.

Project Deadline Extended
Reason: Extension of deadline to allow more designs to come in.

Target Market(s)

All ages from as young as 5 to 6 years old to 60 to 70s.

Industry/Entity Type

It Company

Font styles to use
Other font styles liked:
• Fonts should be simple and minimalist. Easy for elderly to read without straining the eyes.

Requirements
Must have
• My logo which I have designed. Designers can feel free to tweak and enhance the design of the logo. The colour is not definite yet. Consumers must know what
• we are selling from the design of the packaging without guessing how it look
• like. The suggested packaging dimension is 17cm (W) by 23.5cm (H).
Nice to have
• We are looking to print the package using kraft paper which I have attached.
Should not have
• religious inclination of motifs, logo etc.

```html
<!DOCTYPE html>
<html lang="en">
<head>
<meta charset="utf-8">
<title>larkwind flakies – pouch front views</title>
<link rel="stylesheet" href="https://fonts.googleapis.com/css2?family=Tinos&family=Open+Sans:wght@300;400&family=Archivo+Black&display=swap">
<style>
  :root {
    --kraft: #c9a06a;
    --kraft-dark: #b98d57;
    --kraft-seal: #d4ad78;
    --label-white: #ffffff;
    --brand-red: #c41a2c;
    --brand-red-deep: #a9101f;
    --snack-gold: #d89a2c;
    --snack-amber: #a8651a;
    --ink-dark: #1a1a1a;
    --page: #ffffff;
  }
  * { box-sizing: border-box; margin: 0; padding: 0; }
  html, body { width: 1200px; height: 981px; overflow: hidden; background: var(--page); }
  .canvas { position: relative; width: 1200px; height: 981px; }

  .pouch {
    position: absolute; top: 64px; width: 462px; height: 836px;
    background: var(--kraft); border-radius: 14px 14px 22px 22px;
  }
  .pouch__seal {
    position: absolute; left: 0; right: 0; top: 0; height: 42px;
    background: var(--kraft-seal); border-bottom: 2px solid var(--kraft-dark);
    border-radius: 14px 14px 0 0;
  }
  .pouch--white { left: 104px; }
  .pouch--red { left: 600px; width: 440px; }

  .label { position: absolute; top: 200px; height: 585px; }
  .label--white { left: 37px; width: 384px; background: var(--label-white); }
  .label--red { left: 34px; width: 382px; background: var(--brand-red); }

  .snack-photo {
    position: absolute; border-radius: 46% 52% 48% 50%;
    background: radial-gradient(circle at 40% 40%, var(--snack-gold), var(--snack-amber));
  }

  /* white variant */
  .title-vertical {
    position: absolute; left: 30px; top: 462px; width: 400px;
    transform-origin: left top; transform: rotate(-90deg);
    font-family: "Tinos", serif; font-weight: 400; font-size: 46px; line-height: 54px;
    color: var(--ink-dark); white-space: nowrap;
  }
  .accent-stroke { position: absolute; left: 104px; top: 62px; }
  .brand-mark { position: absolute; display: flex; flex-direction: column; align-items: center; }
  .brand-mark__dot { width: 86px; height: 86px; border-radius: 50%; border: 6px solid var(--brand-red); }
  .brand-mark__name { font-family: "Open Sans", sans-serif; font-weight: 300; font-size: 16px; letter-spacing: 2px; color: var(--brand-red); margin-top: 6px; }
  .label--white .brand-mark { left: 146px; top: 60px; }
  .label--white .snack-photo { left: 124px; top: 305px; width: 178px; height: 150px; }
  .flavour-serif {
    position: absolute; left: 24px; top: 494px;
    font-family: "Tinos", serif; font-size: 25px; color: var(--brand-red);
  }
  .net-weight-stack {
    position: absolute; left: 266px; top: 480px;
    font-family: "Tinos", serif; font-size: 16px; line-height: 1.2; color: #222; text-align: center;
  }

  /* red variant */
  .brand-tile {
    position: absolute; left: 118px; top: 0; width: 148px; height: 154px;
    background: var(--label-white); display: flex; align-items: center; justify-content: center;
  }
  .brand-tile .brand-mark { position: static; }
  .title-horizontal {
    position: absolute; left: 22px; right: 22px; top: 170px; text-align: center;
    font-family: "Open Sans", sans-serif; font-weight: 300; font-size: 38px; color: var(--label-white);
  }
  .underline-stroke { position: absolute; left: 26px; top: 222px; }
  .label--red .snack-photo { left: 105px; top: 265px; width: 156px; height: 146px; }
  .flavour-badge {
    position: absolute; left: 112px; top: 470px; width: 142px; height: 40px;
    background: var(--label-white); display: flex; align-items: center; justify-content: center;
    font-family: "Archivo Black", sans-serif; font-size: 22px; color: var(--brand-red-deep);
  }
  .net-weight-line {
    position: absolute; left: 0; right: 0; top: 522px; text-align: center;
    font-family: "Tinos", serif; font-size: 15px; color: var(--label-white);
  }
</style>
</head>
<body>
<main class="canvas">
  <section class="pouch pouch--white" aria-label="larkwind flakies pouch, white label">
    <div class="pouch__seal"></div>
    <div class="label label--white">
      <h1 class="title-vertical">larkwind flakies</h1>
      <svg class="accent-stroke" width="20" height="420" viewBox="0 0 20 420" aria-hidden="true">
        <path d="M4 0 C 10 130, 14 280, 12 420" stroke="var(--brand-red)" stroke-width="4" fill="none" stroke-linecap="round"/>
      </svg>
      <div class="brand-mark">
        <span class="brand-mark__dot"></span>
        <span class="brand-mark__name">larkwind</span>
      </div>
      <div class="snack-photo" role="img" aria-label="Photo of two golden fried flower-shaped crisps"></div>
      <p class="flavour-serif">ORIGINAL</p>
      <p class="net-weight-stack">net weight<br>70grams</p>
    </div>
  </section>

  <section class="pouch pouch--red" aria-label="larkwind flakies pouch, red label">
    <div class="pouch__seal"></div>
    <div class="label label--red">
      <div class="brand-tile">
        <div class="brand-mark">
          <span class="brand-mark__dot"></span>
          <span class="brand-mark__name">larkwind</span>
        </div>
      </div>
      <h1 class="title-horizontal">larkwind flakies</h1>
      <svg class="underline-stroke" width="330" height="20" viewBox="0 0 330 20" aria-hidden="true">
        <path d="M2 16 C 90 8, 220 4, 328 2" stroke="var(--label-white)" stroke-width="4" fill="none" stroke-linecap="round"/>
      </svg>
      <div class="snack-photo" role="img" aria-label="Photo of two golden fried flower-shaped crisps"></div>
      <p class="flavour-badge">ORIGINAL</p>
      <p class="net-weight-line">net weight 70grams</p>
    </div>
  </section>
</main>
</body>
</html>
```